LSV AUDITION

I need a post card design (front only) with this on it:
Leap Spin Vibe (this is the main title to be in all caps)
Auditions
Date: Thursday June 30th
6:30-8:30 PM in person
Address: 4170 Wexley BLVD, Oakland CA 94611
video submissions turn in by Sunday July 3rd, 2022 email:LeapSpinVibe22@trovemail.net
Teens and Adults welcomed

SO PLEASE COME UP WITH A DESIGN THATS COLORFUL AND INVITING THX!

```html
<!DOCTYPE html>
<html lang="en">
<head>
<meta charset="utf-8">
<title>Leap Spin Vibe Auditions</title>
<link href="https://fonts.googleapis.com/css2?family=Montserrat:wght@200;300;800;900&family=Roboto:wght@400;500&display=swap" rel="stylesheet">
<style>
  :root {
    --navy: #0d0830;
    --deep: #1b1a5c;
    --blue: #2c48a8;
    --violet: #6a3aa8;
    --magenta: #c23a9e;
    --plum: #3b1450;
    --white: #ffffff;
    --gold: #e8c46a;
    --pink: #e6a0d2;
    --muted: #8f77a6;
    --panel: rgba(10, 6, 40, 0.88);
  }
  * { margin: 0; padding: 0; box-sizing: border-box; }
  html, body { width: 816px; height: 1200px; overflow: hidden; background: var(--deep); }
  .postcard {
    position: relative;
    width: 816px;
    height: 1200px;
    overflow: hidden;
    font-family: "Roboto", sans-serif;
    color: var(--white);
    background:
      radial-gradient(circle at 30% 72%, rgba(90, 150, 230, 0.55) 0, rgba(90, 150, 230, 0) 22%),
      radial-gradient(circle at 78% 50%, rgba(214, 70, 170, 0.85) 0, rgba(214, 70, 170, 0) 45%),
      radial-gradient(circle at 45% 55%, rgba(140, 110, 210, 0.7) 0, rgba(140, 110, 210, 0) 40%),
      radial-gradient(circle at 25% 20%, var(--blue) 0, rgba(44, 72, 168, 0) 60%),
      linear-gradient(180deg, var(--deep) 0%, var(--violet) 55%, var(--plum) 100%);
  }
  .dancer-photo {
    position: absolute;
    left: 70px;
    top: 448px;
    width: 512px;
    height: 592px;
    border-radius: 45% 45% 30% 30%;
    background: radial-gradient(ellipse at 50% 45%, rgba(245, 242, 250, 0.9) 0, rgba(220, 215, 240, 0.6) 30%, rgba(110, 80, 190, 0.45) 60%, rgba(110, 80, 190, 0) 75%);
  }
  .title-line {
    position: absolute;
    left: 88px;
    top: 36px;
    font-family: "Montserrat", sans-serif;
    font-weight: 200;
    font-size: 258px;
    line-height: 1;
    letter-spacing: -4px;
    color: var(--white);
  }
  .title-accent {
    position: absolute;
    left: 438px;
    top: 258px;
    font-family: "Montserrat", sans-serif;
    font-weight: 800;
    font-size: 106px;
    line-height: 1;
    background: linear-gradient(90deg, #ffffff 0%, #fff6dc 35%, var(--gold) 55%, #ffffff 80%);
    -webkit-background-clip: text;
    background-clip: text;
    color: transparent;
  }
  .big-letter {
    position: absolute;
    font-family: "Montserrat", sans-serif;
    font-weight: 800;
    font-size: 252px;
    line-height: 1;
    color: var(--white);
  }
  .big-v { left: 238px; top: 256px; }
  .big-i { left: 530px; top: 358px; }
  .big-b { left: 150px; top: 556px; }
  .big-e { left: 580px; top: 572px; }
  .auditions {
    position: absolute;
    left: 272px;
    top: 794px;
    font-family: "Roboto", sans-serif;
    font-weight: 500;
    font-size: 32px;
    line-height: 1;
    letter-spacing: 13px;
    color: var(--navy);
    white-space: nowrap;
  }
  .details {
    position: absolute;
    left: 88px;
    top: 849px;
    width: 640px;
    background: var(--panel);
  }
  .details-row {
    height: 57px;
    display: flex;
    align-items: center;
    justify-content: center;
    border-bottom: 1px solid rgba(170, 110, 220, 0.6);
  }
  .details-row:last-child { border-bottom: none; }
  .details-date { color: var(--pink); font-size: 39px; font-weight: 500; }
  .details-date sup { font-size: 20px; }
  .details-time { font-size: 32px; font-weight: 500; }
  .details-address { font-size: 22px; }
  .video-icon { position: absolute; left: 56px; top: 1030px; }
  .video-note {
    position: absolute;
    left: 155px;
    top: 1043px;
    font-size: 25px;
    font-weight: 500;
    white-space: nowrap;
  }
  .email {
    position: absolute;
    left: 123px;
    top: 1084px;
    font-size: 36px;
    font-weight: 500;
    white-space: nowrap;
  }
  .audience {
    position: absolute;
    left: 274px;
    top: 1133px;
    font-size: 25px;
    font-weight: 500;
    color: var(--muted);
    white-space: nowrap;
  }
</style>
</head>
<body>
<main class="postcard">
  <div class="dancer-photo" role="img" aria-label="Photo of a dancer in white leaping with arms raised, holding a flowing purple scarf"></div>

  <h1 class="title">
    <span class="title-line">LEAP</span>
    <span class="title-accent">SPIN</span>
    <span class="big-letter big-v">V</span>
    <span class="big-letter big-i">I</span>
    <span class="big-letter big-b">B</span>
    <span class="big-letter big-e">E</span>
  </h1>

  <p class="auditions">AUDITIONS</p>

  <section class="details">
    <div class="details-row details-date">Date: Thursday June 30<sup>th</sup></div>
    <div class="details-row details-time">6:30-8:30 PM in person</div>
    <div class="details-row details-address">Address: 4170 Wexley BLVD, Oakland CA 94611</div>
  </section>

  <svg class="video-icon" width="76" height="58" viewBox="0 0 76 58" aria-hidden="true">
    <g transform="rotate(-6 38 29)">
      <rect x="4" y="6" width="68" height="46" rx="3" fill="#f4e6b8" stroke="#c9a24a" stroke-width="2"/>
      <rect x="8" y="10" width="7" height="6" fill="#2a1e4a"/>
      <rect x="8" y="26" width="7" height="6" fill="#2a1e4a"/>
      <rect x="8" y="42" width="7" height="6" fill="#2a1e4a"/>
      <rect x="61" y="10" width="7" height="6" fill="#2a1e4a"/>
      <rect x="61" y="26" width="7" height="6" fill="#2a1e4a"/>
      <rect x="61" y="42" width="7" height="6" fill="#2a1e4a"/>
      <path d="M31 19 L48 29 L31 39 Z" fill="#1a1238"/>
    </g>
  </svg>
  <p class="video-note">video submissions turn in by Sunday July 3rd, 2022</p>
  <p class="email">email: LeapSpinVibe22@trovemail.net</p>
  <p class="audience">Teens and Adults welcomed</p>
</main>
</body>
</html>
```